Tallymint - A/B testing for professionals

We need to improve the presentation layer (design only) of our tool tallymint.example.

www.tallymint.example is a A/B testing tool for websites and all kind of applications. The most important features are already listed on our actual webpage and the attached screenshots.
the animated icons on the front page should be included into the design and should match the color scheme. if you think you need to add a logo or similar things to it - feel free to offer us good proposals. you can reach us by sending us a mail to: support@tallymint.example

our needs listed:
-we'd rather have a very good improvement of the actual design instead of a big redesign with all colours changed etc.
- the pages in the screenshots attached should be redesigned. The amount of different layouts will be around 2 - 4 depending on the design.
- the animated icons on www.tallyrmint.example must be included into the design.
- the colors should match with the animated icons.
- we won't need any code. Psd / ai / graphic files only.

Target Market(s)

everyone who sells something with their webpage / application.

Number of Pages Required

3 page

Colors
85cae6
3276b5
85abd2
cee9f5
eaf1f7
0455a3
000000
0492cd

Requirements
Must have
• - animated icons included on the main page.
• - color match with the animated icons on our website or good proposal for adjusting them accordingly.
• - touch of that is highly scaleable and adjustable: we invented a new query language for the project
• - sweetness of the modern web projects and libraries
• - touch that the date are not shared between different users - high value on privacy
Nice to have
• - proposal for a matching logo or including the actual properly
Should not have
• - images people in the design
• - coded versions

```html
<!DOCTYPE html>
<html lang="en">
<head>
<meta charset="utf-8">
<title>Tallymint – A/B testing made for professionals</title>
<link href="https://fonts.googleapis.com/css2?family=Open+Sans:wght@300;400;600;700&family=Alfa+Slab+One&display=swap" rel="stylesheet">
<style>
:root{
  --sky:#85cae6;
  --blue:#3276b5;
  --steel:#85abd2;
  --ice:#cee9f5;
  --mist:#eaf1f7;
  --navy:#0455a3;
  --ink:#000000;
  --cyan:#0492cd;
  --text:#4a4a4a;
  --white:#ffffff;
}
*{margin:0;padding:0;box-sizing:border-box}
html,body{width:1200px;height:3543px;overflow:hidden}
body{position:relative;font-family:"Open Sans",Arial,sans-serif;color:var(--text);background:var(--white)}
.abs{position:absolute}

/* top bar */
.topbar{left:0;top:0;width:1200px;height:52px;background:var(--blue)}
.brand{left:72px;top:8px;font-size:30px;font-weight:600;color:var(--white)}
.nav-btn{top:11px;height:34px;border:2px solid var(--white);border-radius:17px;color:var(--white);font-size:15px;font-weight:600;display:flex;align-items:center;justify-content:center}

/* hero */
.hero{left:0;top:52px;width:1200px;height:1023px;background:linear-gradient(180deg,var(--mist) 0%,#e3eef6 45%,var(--white) 62%,var(--ice) 80%,var(--sky) 100%)}
.hero-rays{left:0;top:700px;width:1200px;height:375px}
.hero-title{left:0;top:88px;width:1200px;text-align:center;font-size:72px;font-weight:300;color:#555}
.hero-title b{font-weight:600}
.hero-sub{left:0;top:170px;width:1200px;text-align:center;font-size:29px;font-weight:300;color:#555}
.hero-cta{left:487px;top:225px;width:226px;height:46px;border:3px solid var(--blue);border-radius:23px;background:var(--white);color:var(--blue);font-size:19px;font-weight:600;display:flex;align-items:center;justify-content:center}
.hero-note{left:0;top:290px;width:1200px;text-align:center;font-size:19px;color:#666}

.monitor{left:100px;top:332px;width:1000px;height:568px;background:#111;border-radius:24px}
.screen{left:136px;top:370px;width:928px;height:460px;background:var(--white)}
.screen-media{left:556px;top:0;width:372px;height:224px;background:#e4e4e4;display:flex;align-items:center;justify-content:center;font-size:22px;font-weight:600;color:#999}
.screen-heading{left:36px;top:110px;font-size:42px;color:#333}
.screen-mark{left:36px;top:158px;font-size:42px;color:#6ab;background:#4aa7a7;color:#7fc9c9;padding:0 6px}
.devtools{left:0;top:214px;width:928px;height:160px;background:linear-gradient(180deg,#dfe6ee,#f4f6f8);}
.screen-tab{top:414px;width:204px;height:40px;border-radius:20px;background:var(--ice);color:var(--navy);font-size:16px;font-weight:600;display:flex;align-items:center;justify-content:center}
.stand{left:450px;top:898px;width:300px;height:150px}

/* intro */
.intro{left:0;top:1108px;width:1200px;text-align:center;font-size:25px;line-height:38px;color:#555}

/* feature circles */
.feature{width:350px;height:350px;border-radius:50%;background:var(--mist);text-align:center;padding:0 48px}
.feature-icon{position:absolute;left:123px;top:20px;width:104px;height:104px;border-radius:50%;background:var(--white);border:2px solid var(--ice)}
.feature-icon span{position:absolute;left:26px;top:26px;width:52px;height:52px;border-radius:50%;background:linear-gradient(135deg,var(--sky),var(--steel))}
.feature h3{margin-top:138px;font-family:"Alfa Slab One",Georgia,serif;font-weight:400;font-size:20px;letter-spacing:5px;color:var(--cyan)}
.feature p{margin-top:12px;font-size:16px;line-height:24px;color:#555}

/* showcase bands */
.band{left:0;width:1200px;height:372px}
.band h2{font-family:"Alfa Slab One",Georgia,serif;font-weight:400;font-size:21px;line-height:32px;letter-spacing:6px;color:var(--cyan);text-align:center}
.band p{margin-top:30px;font-size:15.5px;line-height:25px;color:#555;text-align:center}
.band-copy{top:70px;width:440px}
.band-art{border-radius:50%/40%}

/* footer */
.footer{left:0;top:3156px;width:1200px;height:387px;background:var(--navy);color:var(--white)}
.talk{left:78px;top:40px;font-size:36px;font-weight:300;line-height:40px}
.f-label{font-size:11px;letter-spacing:1px;text-transform:uppercase;color:#cfe0f2}
.f-value{font-size:17px;line-height:24px}
.msg-btn{left:928px;top:120px;width:122px;height:32px;border-radius:16px;background:var(--steel);color:var(--white);font-size:13px;font-weight:700;display:flex;align-items:center;justify-content:center}
.social{top:175px;width:34px;height:34px;border-radius:50%;border:2px solid var(--white)}
.f-col h4{font-size:12px;font-weight:400;letter-spacing:1px;text-transform:uppercase;color:#cfe0f2;margin-bottom:8px}
.f-col a{display:block;color:var(--white);text-decoration:none;font-size:17px;line-height:33px}
.copyright{left:78px;top:318px;font-size:14px;line-height:19px}
</style>
</head>
<body>

<div class="abs topbar"></div>
<div class="abs brand">Tallymint</div>
<div class="abs nav-btn" style="left:868px;width:130px">INSTALL</div>
<div class="abs nav-btn" style="left:1000px;width:130px">LOGIN</div>

<section class="abs hero">
  <svg class="abs hero-rays" viewBox="0 0 1200 375" preserveAspectRatio="none" aria-hidden="true">
    <polygon points="0,80 520,230 0,375" fill="#b4def0" opacity=".6"/>
    <polygon points="1200,80 680,230 1200,375" fill="#b4def0" opacity=".6"/>
    <polygon points="420,375 540,230 660,230 780,375" fill="#ffffff" opacity=".55"/>
  </svg>
  <h1 class="abs hero-title">Tally<b>mint</b></h1>
  <p class="abs hero-sub">A/B testing made for professionals.</p>
  <div class="abs hero-cta">Install &amp; Configure</div>
  <p class="abs hero-note">Start improving your conversion rate</p>
</section>

<div class="abs monitor"></div>
<div class="abs screen">
  <div class="abs screen-media">500x500</div>
  <div class="abs screen-heading">And lastly, this one.</div>
  <div class="abs screen-mark">Checkmate</div>
  <div class="abs devtools" role="img" aria-label="Visual editor inspector panel showing page markup and styles"></div>
  <div class="abs screen-tab" style="left:42px">EDITOR</div>
  <div class="abs screen-tab" style="left:256px">STANDARD REPORTS</div>
  <div class="abs screen-tab" style="left:470px">QUERIES</div>
  <div class="abs screen-tab" style="left:684px">CUSTOM REPORTS</div>
</div>
<svg class="abs stand" viewBox="0 0 300 150" aria-hidden="true">
  <defs><linearGradient id="standShade" x1="0" x2="1"><stop offset="0" stop-color="#9ea3a8"/><stop offset=".5" stop-color="#eef0f2"/><stop offset="1" stop-color="#8d9298"/></linearGradient></defs>
  <path d="M80 0 H220 L230 110 Q150 150 70 110 Z" fill="url(#standShade)"/>
</svg>

<p class="abs intro">Tallymint is a testing tool which measures influence of changes made to your website.<br>Probability and statistics will help you to progressively improve.</p>

<div class="abs feature" style="left:73px;top:1222px">
  <div class="feature-icon" role="img" aria-label="Animated editor icon"><span></span></div>
  <h3>CREATE EXPERIMENTS</h3>
  <p>Use the editor to create experiments by changing texts, attributes and styling. Write JavaScript, or do server side experiments.</p>
</div>
<div class="abs feature" style="left:434px;top:1222px">
  <div class="feature-icon" role="img" aria-label="Animated tag icon"><span></span></div>
  <h3>TAGS</h3>
  <p>By tagging your experiments into categories and strategies, you will be able to measure how well the whole improvement strategy works.</p>
</div>
<div class="abs feature" style="left:793px;top:1222px">
  <div class="feature-icon" role="img" aria-label="Animated eye icon"><span></span></div>
  <h3>PREVIEW</h3>
  <p>All users can freely turn on their previewed experiments, which will be visible on the product just like any other user would see it.</p>
</div>
<div class="abs feature" style="left:73px;top:1590px">
  <div class="feature-icon" role="img" aria-label="Animated stacked blocks icon"><span></span></div>
  <h3>FIELDS</h3>
  <p>Any tracking, goals, events or values can be stored in a data field, which will be automatically available in your reports.</p>
</div>
<div class="abs feature" style="left:434px;top:1590px">
  <div class="feature-icon" role="img" aria-label="Animated open book icon"><span></span></div>
  <h3>REPORTS</h3>
  <p>Use our standard reports or create custom reports with widgets using our query language DQL.</p>
</div>
<div class="abs feature" style="left:793px;top:1590px">
  <div class="feature-icon" role="img" aria-label="Animated paper plane icon"><span></span></div>
  <h3>QUERIES</h3>
  <p>Write your own queries, you're able to select all the data which we save and you can use them in the way ou need them.</p>
</div>

<!-- band: create experiments -->
<section class="abs band" style="top:2012px">
  <svg class="abs" style="left:0;top:0" width="1200" height="372" aria-hidden="true">
    <polygon points="0,0 592,0 560,372 0,372" fill="var(--ice)"/>
    <polygon points="560,372 578,200 596,372" fill="var(--steel)"/>
  </svg>
  <div class="abs band-art" style="left:150px;top:70px;width:300px;height:230px;background:linear-gradient(160deg,#f3b3b8,#f7d2b5 50%,var(--sky))" role="img" aria-label="Illustration of a house on a round lawn"></div>
  <div class="abs band-copy" style="left:640px">
    <h2>CREATE EXPERIMENTS<br>DIRECTLY ON THE WEBSITE</h2>
    <p>The installation of Tallymint enables a keyboard shortcut CTRL + ALT + E on the website. Using this shortcut it is easily possible to create lots of experiments. As long as logged in on Tallymint this shortcut will open the editor and it will assist for special desires.</p>
  </div>
</section>

<!-- band: reports -->
<section class="abs band" style="top:2390px">
  <svg class="abs" style="left:0;top:0" width="1200" height="378" aria-hidden="true">
    <polygon points="605,0 1200,0 1200,378 580,378" fill="var(--ice)"/>
    <polygon points="580,378 608,170 630,378" fill="var(--steel)"/>
  </svg>
  <div class="abs band-copy" style="left:108px">
    <h2>CHECK RESULTS WITH<br>AVAILABLE REPORTS</h2>
    <p>There are quite a few reports available to analyse results. Especially the system wide reports which make use of hashtags are really helpful to find out what the users desire. And even if those system reports are insufficient, Tallymint supports custom reports!</p>
  </div>
  <div class="abs band-art" style="left:760px;top:60px;width:300px;height:250px;background:linear-gradient(160deg,#f4f8fb,var(--sky))" role="img" aria-label="Illustration of a large screen showing a bar chart"></div>
</section>

<!-- band: DQL -->
<section class="abs band" style="top:2775px">
  <svg class="abs" style="left:0;top:0" width="1200" height="374" aria-hidden="true">
    <polygon points="0,0 592,0 560,374 0,374" fill="var(--ice)"/>
    <polygon points="532,374 558,230 578,374" fill="var(--steel)"/>
  </svg>
  <div class="abs band-art" style="left:160px;top:60px;width:300px;height:240px;background:linear-gradient(160deg,#f4f7f9,#dfe7ec 50%,var(--sky))" role="img" aria-label="Illustration of small buildings on a round base"></div>
  <div class="abs band-copy" style="left:640px">
    <h2>FLEXIBLE ANALYSIS<br>USING DQL</h2>
    <p>Tallymint introduces a draw query language (DQL) which is more or less the same as SQL with an output solution. This language is easy to learn, and allows reading the users mind by just painting the data in fancy charts!</p>
  </div>
</section>

<footer class="abs footer">
  <div class="abs talk">Let's talk.<br>We love<br>to listen.</div>

  <svg class="abs" style="left:338px;top:40px" width="34" height="34" viewBox="0 0 24 24" aria-hidden="true"><path d="M6.6 10.8a15 15 0 0 0 6.6 6.6l2.2-2.2c.3-.3.7-.4 1-.2 1.1.4 2.3.6 3.6.6.6 0 1 .4 1 1V20c0 .6-.4 1-1 1A17 17 0 0 1 3 4c0-.6.4-1 1-1h3.5c.6 0 1 .4 1 1 0 1.3.2 2.5.6 3.6.1.3 0 .7-.2 1z" fill="none" stroke="#fff" stroke-width="1.4"/></svg>
  <div class="abs" style="left:390px;top:44px"><div class="f-label">Call</div><div class="f-value">1-000-000-0000</div></div>

  <svg class="abs" style="left:586px;top:38px" width="30" height="38" viewBox="0 0 24 30" aria-hidden="true"><path d="M12 2a8 8 0 0 0-8 8c0 6 8 17 8 17s8-11 8-17a8 8 0 0 0-8-8z" fill="none" stroke="#fff" stroke-width="1.6"/><circle cx="12" cy="10" r="3" fill="none" stroke="#fff" stroke-width="1.6"/></svg>
  <div class="abs" style="left:630px;top:44px"><div class="f-label">Visit</div><div class="f-value">Your Company LTD.<br>Street Name, 000000<br>City Name</div></div>

  <svg class="abs" style="left:874px;top:40px" width="34" height="34" viewBox="0 0 24 24" aria-hidden="true"><path d="M4 20l1-5L16 4l4 4L9 19z M14 6l4 4" fill="none" stroke="#fff" stroke-width="1.5" stroke-linejoin="round"/></svg>
  <div class="abs" style="left:928px;top:44px"><div class="f-label">Write</div><div class="f-value">info@yourdomain.com</div></div>
  <div class="abs msg-btn">MESSAGE US</div>
  <div class="abs social" style="left:928px"></div>
  <div class="abs social" style="left:966px"></div>

  <div class="abs f-col" style="left:387px;top:228px"><h4>Documentation</h4><a>Guides</a><a>Query Docs</a><a>Report Docs</a></div>
  <div class="abs f-col" style="left:630px;top:228px"><h4>Information</h4><a>Ask Questions</a><a>Answer Questions</a><a>Official Blog</a></div>
  <div class="abs f-col" style="left:925px;top:228px"><h4>About</h4><a>Privacy</a><a>Contact</a><a>About us</a></div>

  <div class="abs copyright">© 2015 Tallymint.<br>All rights reserved.</div>
</footer>

</body>
</html>
```